DIGITAL MENUS

Hi Odette (This project is for Odette ONLY)Hope you are well. Can you please help me with designing a new menu for me.I've attached my current menu for you. I would like a new layout using photos for each items.You can use same photos as the menu board that you have designed for me before.Layout must be in Landscape form as current menu. JPEG files.

• Hi Odette,
• Ideal layout:
• DISPLAY MENU #1:
• Rice paper Rolls and Spring rolls
• Pho
• DISPLAY MENU #2:
• Noodle Salads
• Rice
• Stirfry Noodles
• DISPLAY MENU #3:
• Drinks
• 1. All soft drinks $3
• 2. Brae Hollin water $3
• 3. T. Varzoni Sparkling water $4.5
• 4. Qualo Water $4.5
• 5. Brindel Ice-Tea $4.5
• 6. Orvane Juices $5
• 7. Kombucha $5
• and Vietnamese Drinks

```html
<!DOCTYPE html>
<html lang="en">
<head>
<meta charset="utf-8">
<title>Display Menu 2 – Noodle Salads, Stirfry, Rice</title>
<link rel="stylesheet" href="https://fonts.googleapis.com/css2?family=Bebas+Neue&family=Archivo:wght@800&display=swap">
<style>
  :root {
    --orange: #f7941d;
    --ink: #111111;
    --panel-light: #f4f4f4;
    --panel-mid: #e6e6e6;
    --page: #ffffff;
  }
  * { margin: 0; padding: 0; box-sizing: border-box; }
  html, body { width: 1200px; height: 1200px; overflow: hidden; background: var(--page); }
  .canvas { position: relative; width: 1200px; height: 1200px; background: var(--page); }
  .menu-board {
    position: absolute; left: 58px; top: 296px; width: 1084px; height: 608px;
    background: radial-gradient(ellipse at 60% 40%, var(--panel-light), var(--panel-mid));
  }
  .section-title, .price, .extras {
    font-family: "Bebas Neue", "Oswald", sans-serif;
  }
  .section-title {
    position: absolute; left: 111px; color: var(--orange);
    font-size: 44px; line-height: 38px; letter-spacing: 0.5px;
  }
  .price {
    position: absolute; left: 111px; color: var(--ink);
    font-size: 36px; line-height: 32px;
  }
  .dish-photo {
    position: absolute; border-radius: 46% 46% 50% 50% / 30% 30% 70% 70%;
    background: radial-gradient(ellipse at 50% 40%, #a86b3c 0%, #d7b478 35%, #7e9a4c 55%, #f4f6f8 72%, rgba(255,255,255,0) 78%);
  }
  .dish-photo.plate {
    border-radius: 18px;
    transform: skewX(-28deg);
    background: radial-gradient(ellipse at 50% 50%, #9a6a3c 0%, #d58a3c 30%, #4f8a3a 50%, #f6f7f9 66%, #eef0f2 100%);
    box-shadow: 0 4px 8px rgba(0,0,0,0.15);
  }
  .dish-name {
    position: absolute; width: 200px; text-align: center;
    font-family: "Archivo", "Arial Black", sans-serif; font-weight: 800;
    font-size: 19px; line-height: 19px; color: var(--ink);
    transform: translateX(-50%);
  }
  .extras {
    position: absolute; left: 108px; top: 491px; width: 479px; height: 41px;
    background: var(--orange); border-radius: 21px; overflow: hidden;
    color: #fff; font-size: 17px; line-height: 15px;
  }
  .extras-label {
    position: absolute; left: 0; top: 0; width: 82px; height: 41px;
    background: var(--ink); border-radius: 21px 0 0 21px;
    text-align: center; padding-top: 5px;
  }
  .extra-item { position: absolute; top: 5px; text-align: center; transform: translateX(-50%); }
  .extra-item .label { font-family: "Archivo", sans-serif; font-weight: 800; font-size: 13px; }
  .divider { position: absolute; left: 108px; width: 985px; height: 2px; background: var(--orange); }
</style>
</head>
<body>
<div class="canvas">
  <div class="menu-board"></div>

  <!-- Noodle salad -->
  <h2 class="section-title" style="top:331px">NOODLE<br>SALAD</h2>
  <p class="price" style="top:410px">$13.50</p>

  <div class="dish-photo" style="left:287px;top:327px;width:177px;height:110px" role="img" aria-label="Bowl of lemongrass beef noodle salad"></div>
  <div class="dish-photo" style="left:495px;top:327px;width:177px;height:110px" role="img" aria-label="Bowl of lemongrass chicken noodle salad"></div>
  <div class="dish-photo" style="left:703px;top:327px;width:177px;height:110px" role="img" aria-label="Bowl of BBQ pork noodle salad"></div>
  <div class="dish-photo" style="left:909px;top:327px;width:177px;height:110px" role="img" aria-label="Bowl of tofu noodle salad"></div>

  <p class="dish-name" style="left:375px;top:448px">1. LEMONGRASS<br>BEEF</p>
  <p class="dish-name" style="left:583px;top:448px">2. LEMONGRASS<br>CHICKEN</p>
  <p class="dish-name" style="left:791px;top:448px">3. BBQ PORK</p>
  <p class="dish-name" style="left:997px;top:448px">4. TOFU</p>

  <div class="extras">
    <div class="extras-label">*ADD<br>EXTRA</div>
    <div class="extra-item" style="left:128px">$2.00<br><span class="label">MEAT</span></div>
    <div class="extra-item" style="left:220px">$1.00<br><span class="label">NOODLES</span></div>
    <div class="extra-item" style="left:337px">$1.50<br><span class="label">VEGETABLES</span></div>
    <div class="extra-item" style="left:436px">$2.00<br><span class="label">TOFU</span></div>
  </div>

  <div class="divider" style="top:541px"></div>

  <!-- Stirfry -->
  <h2 class="section-title" style="top:554px">STIRFRY<br>WITH THICK<br>RICE NOODLES</h2>
  <p class="price" style="top:667px">$15.50</p>

  <div class="dish-photo plate" style="left:385px;top:565px;width:150px;height:100px" role="img" aria-label="Plate of beef stirfry with thick rice noodles"></div>
  <div class="dish-photo plate" style="left:590px;top:565px;width:150px;height:100px" role="img" aria-label="Plate of chicken stirfry with thick rice noodles"></div>
  <div class="dish-photo plate" style="left:795px;top:565px;width:150px;height:100px" role="img" aria-label="Plate of tofu stirfry with thick rice noodles"></div>

  <p class="dish-name" style="left:460px;top:679px">1. BEEF</p>
  <p class="dish-name" style="left:665px;top:679px">2. CHICKEN</p>
  <p class="dish-name" style="left:870px;top:679px">3. TOFU</p>

  <div class="divider" style="top:707px"></div>

  <!-- Rice -->
  <h2 class="section-title" style="top:720px">RICE</h2>
  <p class="price" style="top:758px">$15.50</p>

  <div class="dish-photo plate" style="left:260px;top:724px;width:142px;height:100px" role="img" aria-label="Plate of BBQ beef with rice"></div>
  <div class="dish-photo plate" style="left:469px;top:724px;width:142px;height:100px" role="img" aria-label="Plate of lemongrass chilli chicken with rice"></div>
  <div class="dish-photo plate" style="left:679px;top:724px;width:142px;height:100px" role="img" aria-label="Plate of tofu and vegetables with rice"></div>
  <div class="dish-photo plate" style="left:880px;top:724px;width:142px;height:100px" role="img" aria-label="Plate of fried rice"></div>

  <p class="dish-name" style="left:336px;top:838px">1. BBQ BEEF</p>
  <p class="dish-name" style="left:543px;top:838px">2. LEMONGRASS<br>CHILLI CHICKEN</p>
  <p class="dish-name" style="left:750px;top:838px">3. TOFU &amp; VEGS</p>
  <p class="dish-name" style="left:953px;top:838px">4. FRIED RICE</p>
</div>
</body>
</html>
```